LUMA ATHLETIC - Stationary suite, templates and consistent design across all fields.

Luma Athletic is a start up business focusing on the following:
P - Performance
A - Apparel
C - Compression garments (FlexaTight)
E - Events (speaking tours, coaching clinics, business forums)

I would like a suite of business templates/invoices/letterheads/business cards/ email signatures etc that are consistent with the logo

Target Market(s)

Sports and business community

Industry/Entity Type

Business

Colors
ec1f27
9bcb3b

Requirements
Nice to have
• http://flexatight-example.com.au/
• One of our major products is FlexaTight compression garments. It would be nice to incorporate the blue lightning and running man into the LUMA Athletic stationary. Files can be provided if you think this could work.

```html
<!DOCTYPE html>
<html lang="en">
<head>
<meta charset="utf-8">
<title>Luma Athletic – Business Card</title>
<link rel="stylesheet" href="https://fonts.googleapis.com/css2?family=Open+Sans:ital,wght@0,400;0,700;0,800;1,700&family=Arimo:wght@400&display=swap">
<style>
  :root {
    --brand-red: #cc0000;
    --brand-green: #5f9a35;
    --ink: #111111;
    --text-grey: #555555;
    --paper: #ffffff;
  }
  html, body {
    margin: 0;
    padding: 0;
    overflow: hidden;
    background: var(--paper);
  }
  .card {
    position: relative;
    width: 1200px;
    height: 686px;
    background: var(--paper);
    overflow: hidden;
    font-family: "Open Sans", Arial, sans-serif;
  }
  .brand {
    position: absolute;
    left: 84px;
    top: 168px;
    display: flex;
    align-items: center;
    gap: 16px;
  }
  .brand-dot {
    width: 48px;
    height: 48px;
    border-radius: 50%;
    background: var(--brand-red);
    flex: none;
  }
  .brand-name {
    font-family: "Open Sans", Arial, sans-serif;
    font-weight: 800;
    font-size: 64px;
    line-height: 1;
    letter-spacing: 1px;
    color: var(--brand-red);
  }
  .brand-tagline {
    position: absolute;
    left: 166px;
    top: 302px;
    margin: 0;
    font-family: "Open Sans", Arial, sans-serif;
    font-weight: 700;
    font-style: italic;
    font-size: 22px;
    color: var(--ink);
    letter-spacing: -0.3px;
  }
  .person {
    position: absolute;
    right: 731px;
    top: 420px;
    text-align: right;
  }
  .person-name {
    margin: 0;
    font-weight: 700;
    font-size: 46px;
    line-height: 1.1;
    color: var(--brand-red);
  }
  .person-role {
    margin: 6px 0 0;
    font-size: 25px;
    color: var(--text-grey);
  }
  .contact {
    position: absolute;
    left: 533px;
    top: 372px;
    font-family: "Arimo", Arial, sans-serif;
    color: var(--text-grey);
  }
  .contact-address {
    margin: 0;
    font-style: normal;
    font-size: 32px;
    line-height: 39px;
  }
  .contact-line {
    display: flex;
    align-items: center;
    gap: 22px;
    font-size: 33px;
    height: 49px;
  }
  .contact-line:first-of-type { margin-top: 20px; }
  .contact-icon { width: 40px; height: 40px; flex: none; }
  .partner-mark {
    position: absolute;
    left: 990px;
    top: 566px;
    font-family: "Open Sans", Arial, sans-serif;
    font-weight: 800;
    font-size: 30px;
    color: var(--ink);
  }
  .footer-band {
    position: absolute;
    left: 0;
    bottom: 0;
    width: 1200px;
    height: 49px;
  }
</style>
</head>
<body>
  <main class="card">
    <div class="brand">
      <span class="brand-dot"></span>
      <span class="brand-name">LUMA ATHLETIC</span>
    </div>
    <p class="brand-tagline">Training Wear Recovery Gear Live Coaching</p>

    <section class="person">
      <h1 class="person-name">Dana Reyes</h1>
      <p class="person-role">President</p>
    </section>

    <section class="contact">
      <address class="contact-address">1420 Harbor View Lane<br>Bayside, CA&nbsp;&nbsp;&nbsp;90000</address>
      <div class="contact-line">
        <svg class="contact-icon" viewBox="0 0 40 40" aria-hidden="true">
          <circle cx="20" cy="20" r="19" fill="var(--brand-red)"/>
          <path d="M14 10 q-5 3 -2 10 q4 8 11 10 q4 1 6 -3 l-4 -4 l-3 2 q-5 -3 -6 -8 l3 -2 z" fill="#fff"/>
        </svg>
        <span>555 014 2278</span>
      </div>
      <div class="contact-line">
        <svg class="contact-icon" viewBox="0 0 40 40" aria-hidden="true">
          <rect x="2" y="9" width="36" height="24" fill="var(--brand-red)"/>
          <polyline points="3,10 20,24 37,10" fill="none" stroke="#fff" stroke-width="2"/>
          <line x1="3" y1="32" x2="15" y2="20" stroke="#fff" stroke-width="1.5"/>
          <line x1="25" y1="20" x2="37" y2="32" stroke="#fff" stroke-width="1.5"/>
        </svg>
        <span>dana.reyes@example.com</span>
      </div>
    </section>

    <div class="partner-mark">FlexaTight</div>

    <svg class="footer-band" viewBox="0 0 1200 49" preserveAspectRatio="none" aria-hidden="true">
      <polygon points="0,0 700,0 714,49 0,49" fill="var(--brand-red)"/>
      <polygon points="712,0 1200,0 1200,49 726,49" fill="var(--brand-green)"/>
    </svg>
  </main>
</body>
</html>
```